LearnNest Business Cards

I will be teaching Zephone and Zepad classes to the 55+community.Small groups of 10(max), or individual lessons.Beginner and Advance ClassesTraining Material ProvidedThis is a new business in Florida.I hope to order business cards and brochures.I found sample of business card on Corvaprint - see below. I like the looks of this card, instead of a lighthouseI would like an apple with the red and white stripes. The red and white apple will be my logo. Thank you,Marla Pennick
Target Market(s)
55+ Adults
Industry/Entity Type
Business
Contact Information for Business Card
Diane ApplebyOwner/Instructor772 571-7011iteachdiane@gmail.com
Look and feel
Each slider illustrates characteristics of the customer's brand and the style your logo design should communicate.

```html
<!DOCTYPE html>
<html lang="en">
<head>
<meta charset="utf-8">
<title>LearnNest Business Card</title>
<link href="https://fonts.googleapis.com/css2?family=Open+Sans:wght@400;600;700&display=swap" rel="stylesheet">
<style>
  :root {
    --page-bg: #161616;
    --card-white: #ffffff;
    --card-grey: #e3e3e3;
    --brand-red: #a01d20;
    --brand-red-dark: #7b1416;
    --brand-green: #2f9a3a;
    --brand-pink: #e8878c;
    --text-red: #a31b1f;
  }
  html, body {
    margin: 0;
    width: 1200px;
    height: 900px;
    overflow: hidden;
    background: var(--page-bg);
    font-family: "Open Sans", Arial, sans-serif;
  }
  .canvas {
    position: relative;
    width: 1200px;
    height: 900px;
  }
  .card {
    position: absolute;
    top: 271px;
    width: 449px;
    height: 260px;
    border-radius: 12px;
    overflow: hidden;
  }
  .card-front { left: 144px; }
  .card-back { left: 633px; width: 451px; }
  .card-art {
    position: absolute;
    inset: 0;
    width: 100%;
    height: 100%;
  }
  .brand-mark {
    position: absolute;
    display: flex;
    align-items: center;
    gap: 8px;
    font-weight: 700;
    white-space: nowrap;
  }
  .brand-dot {
    width: 13px;
    height: 13px;
    border-radius: 50%;
    background: currentColor;
  }
  .card-front .brand-mark {
    left: 34px;
    top: 98px;
    font-size: 22px;
    color: var(--text-red);
  }
  .card-back .brand-mark {
    left: 50%;
    top: 94px;
    transform: translateX(-50%);
    font-size: 28px;
    color: var(--brand-pink);
  }
  .contact-block {
    position: absolute;
    left: 196px;
    top: 34px;
  }
  .person-name {
    margin: 0;
    font-size: 19px;
    font-weight: 700;
    color: var(--text-red);
    line-height: 1.2;
  }
  .person-role {
    margin: 1px 0 0;
    font-size: 13px;
    color: var(--brand-green);
  }
  .address {
    margin: 10px 0 0;
    font-size: 12.5px;
    line-height: 1.25;
    color: var(--text-red);
  }
  .contact-list {
    list-style: none;
    margin: 12px 0 0;
    padding: 0;
    font-size: 12px;
    color: var(--brand-green);
  }
  .contact-list li {
    display: flex;
    align-items: center;
    gap: 8px;
    line-height: 17px;
    white-space: nowrap;
  }
  .contact-icon {
    width: 9px;
    height: 9px;
    fill: var(--text-red);
  }
  .website {
    position: absolute;
    left: 0;
    right: 0;
    bottom: 6px;
    margin: 0;
    text-align: center;
    font-size: 12.5px;
    line-height: 17px;
    color: var(--card-white);
  }
</style>
</head>
<body>
<main class="canvas">

  <section class="card card-front" aria-label="Business card front">
    <svg class="card-art" viewBox="0 0 449 260" aria-hidden="true">
      <defs>
        <linearGradient id="frontSheen" x1="0" y1="0" x2="1" y2="1">
          <stop offset="0" stop-color="var(--card-grey)"/>
          <stop offset="0.5" stop-color="var(--card-white)"/>
          <stop offset="1" stop-color="#f4f4f4"/>
        </linearGradient>
      </defs>
      <rect width="449" height="260" fill="var(--brand-red)"/>
      <path d="M0,115 C25,165 70,210 135,220 C165,224 185,205 220,205 C255,205 275,230 325,230 C395,230 432,165 449,115"
            fill="none" stroke="var(--card-white)" stroke-width="4"/>
      <path d="M0,0 H449 V105 C430,160 392,220 322,220 C275,220 255,196 220,196 C185,196 165,214 135,210 C70,200 25,155 0,105 Z"
            fill="url(#frontSheen)"/>
    </svg>

    <div class="brand-mark"><span class="brand-dot"></span>LearnNest</div>

    <div class="contact-block">
      <h1 class="person-name">Marla Pennick</h1>
      <p class="person-role">Owner/Instructor</p>
      <p class="address">1234, Address Goes Here<br>Florida, 123456</p>
      <ul class="contact-list">
        <li>
          <svg class="contact-icon" viewBox="0 0 10 10"><path d="M2.5,0 H7.5 V10 H2.5 Z M3.5,1 V8 H6.5 V1 Z"/></svg>
          555 013-4829
        </li>
        <li>
          <svg class="contact-icon" viewBox="0 0 10 10"><path d="M0,3 Q5,0 10,3 V4.5 H7.5 V3.5 H2.5 V4.5 H0 Z M2,5 H8 L9,9 H1 Z"/></svg>
          555 013-4829
        </li>
        <li>
          <svg class="contact-icon" viewBox="0 0 10 10"><path d="M0,2 H10 V8.5 H0 Z"/><path d="M0.5,2.5 L5,6 L9.5,2.5" fill="none" stroke="#fff" stroke-width="1"/></svg>
          learnnestmarla@mailbox-example.com
        </li>
      </ul>
    </div>

    <p class="website">www.yoursite-example.com</p>
  </section>

  <section class="card card-back" aria-label="Business card back">
    <svg class="card-art" viewBox="0 0 451 260" aria-hidden="true">
      <rect width="451" height="260" fill="var(--brand-red)"/>
      <path d="M0,0 H451 V105 C432,165 400,228 340,228 C298,228 285,206 258,206 C228,206 212,228 178,228 C90,228 30,160 0,105 Z"
            fill="var(--brand-red-dark)"/>
    </svg>
    <div class="brand-mark"><span class="brand-dot"></span>LearnNest</div>
  </section>

</main>
</body>
</html>
```